Invitation - Lumara Holdings Christmas Party 2015

Lumara Holdings Christmas "Block Party" 2015

Brief:
The Lumara Holdings comprises of Lumara, Tesby and KWF. Three separate companies that together offer a complete end to end product development and manufacturing service. We have over 120 employees and we really want to encourage all of them to attend. In years gone by it has been just about going to a bar or restaurant and drinking as much as the staff could. This year we wanted to hold it onsite and get people together with their families to celebrate what we do. We will likely also invite key customers to mingle and enjoy the night. It's going to be held in our car park however the scene will be set with overhead Christmas lights criss crossing the activities below. It's a sort of theme park/block party atmosphere designed to be relaxed and a heap of fun. We will have a DJ playing music all night. Food is from one of Brisbane's best street food vans and we will be running our own wood fired pizza oven all night with the boss cooking up for the staff.

We need an invite that will excite the team and get them to come along. It needs to be classy enough to show what we are trying to achieve with the night and fun enough that the kids can get excited about it too. Heaps of colours and maybe some graphic description of what the nights all about. We will print it on A4 flyers to hand out and also some larger A3 or A2 posters

Event:
We are holding the annual Christmas party this year with a difference. This year it's about getting everyone and their families together. There will be plenty for everyone from the grown ups right down to the little guys.

What's on:

- Full service bar and frozen daiquiris, beer wine and basics
- Brisbane's famous "Chowcart" van will be preparing their amazing gourmet dishes for everyone
- Wood fire pizzas served all night
- Mechanical bull from 5 till 9pm
- Strongman High Striker - prizes to be won
- Door prize raffle entry for each guest
- for the kids there will be a jumping castle (we ordered the giant one incase the big kids wanted to have a go), fairy floss machine and other activities

Times:
4:00-5:00pm - open house, a chance to take your family through the factory to show what we do each day
5:00-9pm - eat, drink and have fun, bring the family and enjoy the night and celebrate a massive year.
RSVP - Friday 23rd October. Strictly by invitation only, Invites are for staff and their immediate families only. All names must be listed on the RSVP as it will be required at the door.

Where : Grand Tent in the car park - 42 Larkspur Lane Hollowfield

When : Sat Nov 7th 4-9pm

PS - it's important that everyone that attends ensures they arrive safely and get home safely, no one should drink and drive and multiple maxi taxis will be available at the end of the night to take people to the city or other nearby locations after the function. Ensure you plan your night well and do not drink and drive. Any food allergies need to be mentioned on your RSVP

Target Market(s)

Staff and their families

Industry/Entity Type

Group

Requirements
Must have
• A really good impact, must get the staff excited and get them to commit to coming along
Nice to have
• It would be great to set the mood in the invite. The lighting on the night will be a major feature. Fairy lights criss crossing the area with the activities below. A bar with hay bales for seating, the mechanical bull in the centre with other activities around the outside. The wood fired pizza over will probably become a place for people to sit and keep warm and the food van parked to one side serving up unreal street food.
Should not have
• No preference

```html
<!DOCTYPE html>
<html lang="en">
<head>
<meta charset="utf-8">
<title>Lumara Holdings Christmas Party Invitation</title>
<link rel="stylesheet" href="https://fonts.googleapis.com/css2?family=Great+Vibes&family=Cousine&family=Tinos&family=Oswald:wght@600&display=swap">
<style>
  :root {
    --plum: #7a0c45;
    --berry: #a3163f;
    --scarlet: #c42a30;
    --snow: #ffffff;
    --frost: rgba(255, 228, 240, 0.62);
    --frost-mid: rgba(255, 214, 232, 0.32);
    --brand-dot: #d8262c;
  }
  html, body {
    margin: 0;
    padding: 0;
    overflow: hidden;
    background: #ffffff;
  }
  .invitation {
    position: relative;
    width: 849px;
    height: 1200px;
    overflow: hidden;
    background: linear-gradient(165deg, var(--plum) 0%, var(--berry) 45%, var(--scarlet) 100%);
    color: var(--snow);
  }
  .brand {
    position: absolute;
    left: 22px;
    top: 24px;
    display: flex;
    align-items: center;
    gap: 7px;
    z-index: 2;
  }
  .brand-dot {
    width: 12px;
    height: 12px;
    border-radius: 50%;
    background: var(--brand-dot);
  }
  .brand-name {
    font-family: "Oswald", sans-serif;
    font-weight: 600;
    font-size: 30px;
    letter-spacing: 1px;
    line-height: 1;
    color: var(--snow);
  }
  .snowflakes {
    position: absolute;
    border-radius: 50%;
  }
  .snowflakes-top {
    left: 360px;
    top: -300px;
    width: 820px;
    height: 900px;
    background: radial-gradient(closest-side, var(--frost) 0%, var(--frost-mid) 45%, rgba(255, 214, 232, 0) 100%);
  }
  .snowflakes-bottom {
    left: -380px;
    top: 660px;
    width: 780px;
    height: 880px;
    background: radial-gradient(closest-side, var(--frost) 0%, var(--frost-mid) 45%, rgba(255, 214, 232, 0) 100%);
  }
  .snowflake-lone {
    left: 28px;
    top: 300px;
    width: 84px;
    height: 84px;
    background: radial-gradient(closest-side, var(--frost-mid) 0%, rgba(255, 214, 232, 0) 100%);
  }
  .details {
    position: absolute;
    left: 0;
    right: 100px;
    top: 440px;
    text-align: center;
    z-index: 1;
  }
  .title {
    margin: 0;
    font-family: "Great Vibes", cursive;
    font-weight: 400;
    font-size: 78px;
    line-height: 1;
    color: var(--snow);
  }
  .tagline {
    margin: 14px 0 12px;
    font-family: "Tinos", serif;
    font-size: 28px;
    line-height: 1.1;
    color: var(--snow);
  }
  .info {
    margin: 0;
    font-family: "Cousine", monospace;
    font-size: 24px;
    line-height: 39px;
    color: var(--snow);
  }
</style>
</head>
<body>
  <main class="invitation">
    <div class="snowflakes snowflakes-top" role="img" aria-label="Cluster of white lacy snowflakes filling the top right corner"></div>
    <div class="snowflakes snowflakes-bottom" role="img" aria-label="Cluster of white lacy snowflakes filling the bottom left corner"></div>
    <div class="snowflakes snowflake-lone" role="img" aria-label="Single small white snowflake"></div>

    <div class="brand">
      <span class="brand-dot"></span>
      <span class="brand-name">Lumara</span>
    </div>

    <section class="details">
      <h1 class="title">Christmas Party</h1>
      <p class="tagline">Eat, Drink, Games and Door Prize</p>
      <p class="info">Saturday, November 7th<br>4 PM Until 9 PM<br>Grand Tent in the car park<br>42 Larkspur Lane Hollowfield</p>
    </section>
  </main>
</body>
</html>
```